Nootropic Supplement Label Design

Hello everyone! Thanks for looking at our project.

We are need a really cool label design that stands out, but also remains slick and clean. We will of course want finished AI / PDF files for any minor text edits, and to send to print.

Product type: Nootropics. (think sorvane pill from the movie)
Brand Name: Vantrel (logo will be provided)
Product Name: Quadrelle
Tagline: Vantrelly Charged Nootropics (to be placed under logo)
Slogan: Go Boundfree

We would like the brand name logo to not be so big, more focus on the name Quadrelle.

Would like some type of Neuron design, something that cool. This product is going to enhance brain function that is why. This part should be kind of bright / neon looking as we might have it shiny or holographic on the print.

Colors, we are open to anything.

Fonts, we like cool for the name of the product, but professional and clean for the most part.

The bottle will be a normal white bottle that holds capsules. Please provide the design with the bottle as well.

Supplement Facts just put random things on this. We typically like it to be transparent with the background. Instead of a white box with black font.

Buzzwords that you can include:
Enhances:
Mental Focus
Clarity
Memory

PLEASE NOTE ON THE LOGO, THE BLUE VANTREL SYMBOL COLOR CAN BE CHANGED TO WHAT YOU WANT IT TO BE :D

Have it match whatever color scheme you do. Thank you!

Example of another companies design. https://www.brightcapsulehub.example/image/cache/data/ko/Sorvane/481937260548-1-750x750.jpg

We do not want a design like this, just showing example. This is probably considered the coolest one on the market vs other Nootropic products. We want to stand out too. :)

Target Market(s)

18-30 College Millienials

Industry/Entity Type

Nutrition

Font styles to use
Sans Serif

Requirements
Must have
• Logo provided.
Nice to have
• Neruon transmitter type design on the label.
Should not have
• Plain white label.

```html
<!DOCTYPE html>
<html lang="en">
<head>
<meta charset="utf-8">
<title>Quadrelle Label</title>
<link rel="stylesheet" href="https://fonts.googleapis.com/css2?family=Questrial&family=Roboto:wght@400;700&family=Roboto+Condensed:wght@400&display=swap">
<style>
  :root {
    --stage: #aeb0b2;
    --label-dark: #0b1418;
    --label-deep: #0f2a30;
    --teal: #2a6f78;
    --teal-light: #9fc9cf;
    --aqua-bar: #3fd2d4;
    --blue-pill: #1f7ecb;
    --text-light: #ffffff;
    --text-dark: #16252c;
  }
  * { box-sizing: border-box; margin: 0; padding: 0; }
  html, body { width: 1200px; height: 1143px; overflow: hidden; }
  body {
    background: radial-gradient(ellipse at 50% 45%, #c4c6c8 0%, var(--stage) 70%);
    font-family: "Questrial", sans-serif;
    position: relative;
  }
  .label {
    position: absolute;
    left: 30px; top: 368px;
    width: 1140px; height: 407px;
    overflow: hidden;
    background: linear-gradient(90deg, var(--label-dark) 0%, var(--label-deep) 30%, #10333a 50%, var(--label-deep) 70%, var(--label-dark) 100%);
    color: var(--text-light);
  }
  .label-art {
    position: absolute; inset: 0;
    background:
      radial-gradient(ellipse 300px 300px at 569px 150px, rgba(5,10,12,0.95) 0%, rgba(8,20,24,0.85) 70%, rgba(0,0,0,0) 100%),
      linear-gradient(180deg, rgba(0,0,0,0) 60%, rgba(42,120,130,0.5) 100%),
      radial-gradient(ellipse 600px 200px at 569px 420px, rgba(60,160,170,0.55), rgba(0,0,0,0) 70%);
  }
  .light-band {
    position: absolute; left: 0; right: 0; top: 209px; height: 94px;
    background: linear-gradient(90deg, rgba(120,180,190,0.15) 0%, rgba(200,225,230,0.85) 30%, rgba(225,238,241,0.95) 50%, rgba(200,225,230,0.85) 70%, rgba(120,180,190,0.15) 100%);
  }
  .facts {
    position: absolute; left: 25px; top: 58px; width: 244px; height: 296px;
    border: 3px solid rgba(170,190,195,0.75);
    padding: 5px 8px;
    font-family: "Roboto", sans-serif;
    font-size: 11.5px;
    line-height: 1.3;
  }
  .facts h2 { font-family: "Roboto", sans-serif; font-weight: 700; font-size: 21px; line-height: 1.1; }
  .facts .bar { height: 14px; background: var(--aqua-bar); margin: 5px 0 6px; }
  .facts .bar.thin { height: 7px; margin: 2px 0 4px; }
  .facts .row { display: flex; justify-content: space-between; }
  .facts .right { text-align: right; font-size: 10px; font-weight: 700; }
  .facts .small { font-size: 9px; line-height: 1.2; margin-top: 2px; }
  .facts .small + .small { margin-top: 6px; }
  .facts b { font-weight: 700; }
  .facts .rule { border-bottom: 1px solid rgba(255,255,255,0.6); }
  .brand {
    position: absolute; left: 0; width: 1138px; top: 30px; text-align: center;
  }
  .brand-name {
    display: inline-flex; align-items: center; gap: 8px;
    font-size: 27px; letter-spacing: 1px; color: var(--text-light);
  }
  .brand-dot { width: 12px; height: 12px; border-radius: 50%; background: var(--blue-pill); }
  .brand-tagline {
    width: 160px; margin: 3px auto 0; padding-top: 2px;
    border-top: 1px solid rgba(255,255,255,0.6);
    font-family: "Roboto Condensed", sans-serif; font-size: 6px; letter-spacing: 0.3px; text-transform: uppercase;
  }
  .product-name {
    position: absolute; left: 0; width: 1138px; top: 88px;
    text-align: center; font-size: 56px; letter-spacing: 1px; color: var(--text-light);
  }
  .slogan {
    position: absolute; left: 502px; top: 160px; width: 252px; height: 30px;
    border-radius: 0 15px 15px 0;
    background: linear-gradient(90deg, rgba(31,126,203,0) 0%, rgba(31,126,203,0.5) 40%, var(--blue-pill) 100%);
    color: var(--text-dark); text-align: right; padding-right: 16px;
    font-size: 18px; line-height: 30px; letter-spacing: 1px; text-transform: uppercase;
  }
  .benefits {
    position: absolute; left: 0; width: 1138px; top: 218px;
    text-align: center; list-style: none; color: var(--text-dark);
    font-size: 18px; line-height: 26px; letter-spacing: 1.5px; text-transform: uppercase;
  }
  .divider { position: absolute; left: 382px; width: 373px; top: 318px; height: 2px; background: #e8f2f4; }
  .supplement-type {
    position: absolute; left: 0; width: 1138px; top: 331px; text-align: center;
    font-size: 14px; letter-spacing: 1px; text-transform: uppercase;
  }
  .count {
    position: absolute; left: 486px; top: 360px; width: 158px; height: 30px;
    background: #fff; border-radius: 15px; color: var(--text-dark);
    text-align: center; line-height: 30px; font-size: 14px; letter-spacing: 1px; text-transform: uppercase;
  }
  .description {
    position: absolute; left: 866px; top: 72px; width: 236px;
    font-family: "Roboto", sans-serif; font-size: 12px; line-height: 15px; text-align: center;
  }
  .description p + p { margin-top: 14px; }
</style>
</head>
<body>
  <section class="label">
    <div class="label-art" role="img" aria-label="Dark teal background with glowing neuron and molecule network"></div>
    <div class="light-band"></div>

    <div class="facts">
      <h2>Supplement Facts</h2>
      <div>Serving size 1 - 2 teaspoon (10g)</div>
      <div>Serving per container about 15</div>
      <div class="bar"></div>
      <div class="rule" style="font-size:10px;font-weight:700">Amount per serving</div>
      <div class="row"><span><b>Calories</b>&nbsp;&nbsp;&nbsp;44.81</span><span>Calories from fat 0</span></div>
      <div class="bar thin"></div>
      <div class="right">% Daily Value*</div>
      <div class="row"><span><b>Total Fat</b>&nbsp;&nbsp;.03g</span><b>?%</b></div>
      <div class="row"><span><b>Sodium</b> 10.18mg</span><b>?%</b></div>
      <div class="row"><span><b>Total Carbohydrate</b> 0g</span><b>0%</b></div>
      <div class="row"><span><b>Protein</b> 11.14g</span><b>?%</b></div>
      <div class="bar"></div>
      <p class="small">*Percent Daily Values (DV) are based on a 2,000 calorie diet</p>
      <p class="small">Not a significant source of calories from fat, saturated fat, trans fat, cholesterol, dietary fiber, sugar, Vitamin A, vitamin C, Calcium and iron.</p>
    </div>

    <div class="brand">
      <div class="brand-name"><span class="brand-dot"></span>VANTREL</div>
      <div class="brand-tagline">Vantrelly Charged Nootropics</div>
    </div>
    <h1 class="product-name">QUADRELLE</h1>
    <div class="slogan">Go Boundfree</div>

    <ul class="benefits">
      <li>Extreme Focus</li>
      <li>Crystal Clear Clarity</li>
      <li>Improved Memory</li>
    </ul>
    <div class="divider"></div>
    <div class="supplement-type">Dietary Supplement</div>
    <div class="count">60 Capsules</div>

    <div class="description">
      <p>Lorem ipsum dolor sit amet, magna decore dicunt eu mel, cu eos magna laudem. Adhuc ridens accumsan sit in, ex eos movet eruditi ornatus. Cu qui aeque quaeque vulputate, ipsum deleniti eleifend est an. Possit eirmod eam at, sea cu probo maiestatis, solum modus vel ne. Ad pri inciderint interpretaris.</p>
      <p>Etiam invenire deterruisset usu in, vix at omnesque ponderum, vix et ferri errem gubergren. Noluisse accommodare an pro, eu eos purto tacimates rationibus. Idque affert reformidans ea per. Eros commune ei nam. Cu qui ponderum explicari.</p>
    </div>
  </section>
</body>
</html>
```